Business Card Design for Tolvane Holdings

I need a business card designed for Tolvane Holdings. I would like basic contact info and would like the card to be a bit modern but not childish. We manage several companies so it needs to look very professional. Watermark is cool and a plan logo maybe offset on the other side but I will leave the design up to you. I would like to see both color and grey scale designs. This is my first time using Pixel Bazaar so hopefully we get some great results! Future projects available for the selected designer potentially.

Target Market(s)

Tolvane Holdings owns several companies serving the software, real estate and automotive industry

Industry/Entity Type

Business

Contact Information for Business Card

Gordon P. Lask
512.608.2247
gordon.p.lask@mailbrook.net

Font styles to use
Serif

Requirements
Must have
• contact information listed on card details
Nice to have
• I am open to letting you use your creative mind to design the best eye catching cards.

```html
<!DOCTYPE html>
<html lang="en">
<head>
<meta charset="utf-8">
<title>Tolvane Holdings – Business Card</title>
<link href="https://fonts.googleapis.com/css2?family=Arimo:wght@400;700&display=swap" rel="stylesheet">
<style>
  :root {
    --backdrop: #2e2e2e;
    --paper: #ffffff;
    --paper-shade: #f1f3f4;
    --band: #0a8fc0;
    --band-deep: #0678a6;
    --mark-dark: #1d4f9a;
    --mark-light: #5fbfe0;
    --faint-mark: #c8e6f1;
    --faint-circle: #dde9f2;
    --name-light: #e4e8ea;
    --ink: #1f2a33;
  }
  * { margin: 0; padding: 0; box-sizing: border-box; }
  html, body {
    width: 1200px; height: 873px; overflow: hidden;
    background: var(--backdrop);
    font-family: "Arimo", Arial, sans-serif;
  }
  .stage { position: relative; width: 1200px; height: 873px; }

  .card {
    position: absolute;
    width: 540px; height: 309px;
    background: linear-gradient(180deg, var(--paper) 0%, var(--paper-shade) 100%);
    overflow: hidden;
    box-shadow: 0 10px 30px rgba(0,0,0,.45);
  }

  /* Back side */
  .card-back { left: 60px; top: 110px; }
  .watermark {
    position: absolute; inset: 0;
    display: flex; align-items: center; justify-content: center; gap: 18px;
  }
  .watermark-circle {
    width: 150px; height: 150px; border-radius: 50%;
    background: var(--faint-circle);
  }
  .watermark-name {
    font-size: 34px; font-weight: 700; color: var(--faint-mark);
    line-height: 1.1; width: 210px;
  }

  /* Front side */
  .card-front { left: 600px; top: 450px; }
  .brand {
    position: absolute; top: 44px; left: 0; right: 0;
    display: flex; align-items: center; justify-content: center; gap: 12px;
  }
  .brand-circle {
    width: 54px; height: 54px; border-radius: 50%;
    background: var(--mark-dark);
  }
  .brand-name {
    font-size: 24px; font-weight: 700; color: var(--mark-dark);
  }
  .rule {
    position: absolute; left: 0; right: 0; top: 150px; height: 4px;
    background: var(--band);
  }
  .band {
    position: absolute; left: 0; right: 0; top: 160px; bottom: 0;
    background: linear-gradient(180deg, var(--band) 0%, var(--band-deep) 100%);
  }
  .holder {
    position: absolute; top: 126px; left: 0; right: 0; text-align: center;
  }
  .holder-name {
    font-size: 21px; font-weight: 700; letter-spacing: .5px;
    color: var(--mark-dark);
  }
  .holder-title {
    font-size: 15px; color: var(--ink); margin-top: 12px;
  }
  .contact {
    position: absolute; display: flex; align-items: center; gap: 8px;
    font-size: 15px; color: var(--ink);
  }
  .contact svg { width: 14px; height: 14px; flex: none; }
  .contact-email { right: 30px; top: 212px; }
  .contact-phone { left: 30px; bottom: 30px; }
</style>
</head>
<body>
<main class="stage">

  <section class="card card-back" aria-label="Card back">
    <div class="watermark">
      <span class="watermark-circle"></span>
      <span class="watermark-name">Tolvane Holdings</span>
    </div>
  </section>

  <section class="card card-front" aria-label="Card front">
    <div class="brand">
      <span class="brand-circle"></span>
      <span class="brand-name">Tolvane Holdings</span>
    </div>
    <div class="rule"></div>
    <div class="band"></div>
    <div class="holder">
      <p class="holder-name">GORDON P. LASK</p>
      <p class="holder-title">Managing Partner</p>
    </div>
    <p class="contact contact-email">
      <svg viewBox="0 0 14 14" aria-hidden="true">
        <circle cx="7" cy="7" r="7" fill="#e4e8ea"/>
        <rect x="3" y="4.5" width="8" height="5.5" fill="none" stroke="#0678a6" stroke-width="1"/>
        <path d="M3 4.5 L7 8 L11 4.5" fill="none" stroke="#0678a6" stroke-width="1"/>
      </svg>
      gordon.p.lask@mailbrook.net
    </p>
    <p class="contact contact-phone">
      <svg viewBox="0 0 14 14" aria-hidden="true">
        <circle cx="7" cy="7" r="7" fill="#e4e8ea"/>
        <path d="M4.5 3.5 L6 3.5 L6.6 5.4 L5.6 6.1 Q6.6 7.9 8 8.5 L8.7 7.5 L10.5 8.1 L10.5 9.6 Q6 10 4.5 3.5 Z" fill="#0678a6"/>
      </svg>
      512.608.2247
    </p>
  </section>

</main>
</body>
</html>
```